Redesign Digital Lending Mobile App - Android/ Flutter

Want to re-theme an existing Digital Lending Mobile app to simplify customer journeys, as well as uplift the UI.

Most users will have small screen phones so the design needs to take that into consideration while also adapting to those with larger devices, like admins with Tablets.

Have already laid out customer journeys on Figma with guidance on how the flow of the app should be. https://www.plandeck.example/board/q4tRw8KzPmYx2LbNvcHsaT/KovaPay?view-id=3-5120&k=Zu8pRtQwLmNcXbYa-2

Video capture of current app: https://vault.trelmora.example/clip/d/7Hq2WmRtLp9XzKcVbNa4YsDfGe8JuQo3/view
https://vault.trelmora.example/clip/d/4Pn8ZxCvBq1MwLtRyHs6KdJgFa2UeXi9/view

The documented views for Web are also here https://docs.quenlaro.example/open?id=3A8C2D4F6B1E9077!kb2d58e71403a4c6e8f2a91d04b7c3e68&resid=3A8C2D4F6B1E9077!kb2d58e71403a4c6e8f2a91d04b7c3e68&cid=3a8c2d4f6b1e9077&ithint=file%2Cdocx&redeem=bXhZc2RrcVp0TmxhUGVvV2lGcnVHc0JtWWpLdlFhWHpOcHRMZUR3U2JjUmZUeUFnSGxNb1ZpRXVKd0NrRHNYcVBuWmFNYmd5TGVr&migratedtospo=true&wdo=2
Updates

Target Market(s)

Kenya, Tanzania, Uganda - Africa

Industry/Entity Type

Fintech

Requirements
Must have
• Responsive for diff screens, esp. in context of smaller screen smartphone
Nice to have
• Thematic components to ensure new views can easily be adapted to these themse

```html
<!DOCTYPE html>
<html lang="en">
<head>
<meta charset="utf-8">
<title>KovaPay – Lending App Screens</title>
<link href="https://fonts.googleapis.com/css2?family=Montserrat:wght@400;500;600;700&display=swap" rel="stylesheet">
<style>
:root{
  --bg-top:#93b0d4;
  --bg-bottom:#e4e1dc;
  --blue:#2f78c8;
  --blue-soft:#dbe8f7;
  --green:#3f9b5f;
  --green-btn:#449a63;
  --area-light:#d4f3e4;
  --area-dark:#a8dcc9;
  --ink:#111418;
  --muted:#8a9099;
  --line:#e3e6ea;
  --card:#ffffff;
}
*{margin:0;padding:0;box-sizing:border-box}
html,body{width:1200px;height:954px;overflow:hidden}
body{
  font-family:"Montserrat",sans-serif;color:var(--ink);
  background:linear-gradient(180deg,var(--bg-top) 0%,#b9c7d9 55%,var(--bg-bottom) 100%);
  position:relative;
}
.brand{position:absolute;left:0;width:1200px;top:30px;text-align:center}
.brand-dot{width:80px;height:80px;border-radius:50%;background:var(--blue);margin:0 auto 18px}
.brand-name{font-weight:700;font-size:46px;color:var(--blue);letter-spacing:1px}

.screen{position:absolute;background:var(--card);border-radius:28px;overflow:hidden;box-shadow:0 6px 24px rgba(40,60,90,.15)}
.screen *{position:absolute}
.screen-dashboard{left:78px;top:252px;width:278px;height:630px}
.screen-summary{left:439px;top:236px;width:290px;height:646px}
.screen-total{left:823px;top:252px;width:278px;height:599px}

.time{font-size:9px;font-weight:500}
.status{display:flex;gap:6px;align-items:center}
.status svg,.status span{position:static}
.menu{width:19px;height:14px;border-top:2.5px solid var(--ink);border-bottom:2.5px solid var(--ink)}
.menu::after{content:"";position:absolute;left:0;right:0;top:3px;border-top:2.5px solid var(--ink)}
.chat{width:18px;height:18px;border-radius:50%;background:#e9ebee}
.chat::after{content:"0";position:absolute;right:-3px;top:-3px;width:8px;height:8px;border-radius:50%;background:#e8262b;color:#fff;font-size:6px;text-align:center;line-height:8px}
.small-name{font-weight:700;font-size:14px;color:var(--blue);width:100%;text-align:center}
.small-dot{width:24px;height:24px;border-radius:50%;background:var(--blue)}

.stat{background:var(--card);border-radius:4px;box-shadow:0 1px 5px rgba(0,0,0,.12)}
.stat .ico{left:6px;top:8px;width:18px;height:18px;border-radius:50%;background:var(--blue-soft)}
.stat .lbl{left:29px;top:6px;font-size:8px;font-weight:600;white-space:nowrap}
.stat .val{left:31px;top:17px;font-size:8px;font-weight:600;color:var(--blue)}

.heading{font-weight:700;font-size:15px}
.chip{height:16px;border:1px solid #cfd3d8;border-radius:9px;font-size:7.5px;font-weight:500;line-height:14px;padding-left:7px}
.chip::after{content:"";position:absolute;right:6px;top:6px;border:3px solid transparent;border-top:3px solid var(--ink)}

.row-ico{width:22px;height:22px;border-radius:50%;background:var(--blue-soft);border:2px solid var(--blue)}
.row-lbl{font-size:10.5px;font-weight:600;white-space:nowrap}
.row-val{font-size:10.5px;font-weight:600;text-align:right;width:90px}
.bar{left:53px;width:180px;height:4px;border-radius:2px;background:#e6e7e9}
.bar .fill{left:0;top:0;height:4px;border-radius:2px;background:var(--green)}
.bar .knob{top:-3px;width:10px;height:10px;border-radius:50%;background:var(--blue);margin-left:-5px}

.axis{font-size:6px;color:var(--muted);text-align:right;width:28px}
.tick{font-size:6px;color:var(--muted)}

.nav{height:40px;border-radius:20px;background:var(--card);box-shadow:0 2px 8px rgba(0,0,0,.12)}
.nav .it{top:8px;width:24px;height:24px;margin-left:-12px}
.nav .on{top:4px;width:32px;height:32px;margin-left:-16px;border-radius:50%;background:var(--blue);box-shadow:0 3px 6px rgba(47,120,200,.4)}

.search{left:21px;top:57px;width:234px;height:20px;border-radius:10px;background:#eeeff1;font-size:9px;color:var(--muted);line-height:20px;padding-left:14px}
.title{font-weight:600;font-size:19px;text-align:center;width:100%}
.table{left:5px;top:127px;width:279px;height:390px;border:1px solid var(--ink)}
.tr{left:0;width:277px;height:43.2px;border-bottom:1px solid var(--ink)}
.tr:last-child{border-bottom:none}
.tr .row-ico{left:14px;top:11px;width:20px;height:20px}
.tr .k{left:41px;top:14px;font-size:10.5px;font-weight:600;white-space:nowrap}
.tr .v{left:189px;top:14px;font-size:10.5px;font-weight:600;padding-left:11px;border-left:1px solid var(--ink);height:43px;top:0;line-height:43px;width:88px}
.next{left:112px;top:530px;width:64px;height:25px;border-radius:3px;background:var(--green-btn);color:#fff;font-size:9.5px;font-weight:600;text-align:center;line-height:25px}

.big{font-weight:600;text-align:center;width:100%}
.toggle{left:96px;top:192px;width:88px;height:16px;border-radius:8px;background:#e6e7e9;font-size:7.5px;font-weight:600}
.toggle .p{left:0;top:0;width:46px;height:16px;border-radius:8px;background:var(--green-btn);color:#fff;text-align:center;line-height:16px}
.toggle .l{left:58px;top:0;line-height:16px}
.pill{top:232px;height:16px;border:1px solid #cfd3d8;border-radius:8px;font-size:7.5px;font-weight:600;text-align:center;line-height:14px}
.pill.sel{background:#cfe0f4;border-color:#cfe0f4;color:var(--blue)}
.tip{left:151px;top:253px;width:67px;height:36px;background:#fff;box-shadow:0 1px 6px rgba(0,0,0,.15);border-radius:3px}
.tip .a{left:12px;top:5px;font-size:8px;font-weight:500}
.tip .b{left:12px;top:18px;font-size:10px;font-weight:500;color:var(--blue)}
</style>
</head>
<body>

<header class="brand">
  <div class="brand-dot"></div>
  <div class="brand-name">KovaPay</div>
</header>

<!-- Dashboard -->
<section class="screen screen-dashboard">
  <div class="time" style="left:6px;top:38px">11:56 pm</div>
  <div class="status" style="left:216px;top:38px">
    <svg width="12" height="9" viewBox="0 0 12 9"><rect x="0" y="6" width="2" height="3"/><rect x="3" y="4" width="2" height="5"/><rect x="6" y="2" width="2" height="7"/><rect x="9" y="0" width="2" height="9"/></svg>
    <svg width="12" height="9" viewBox="0 0 12 9" fill="none" stroke="#111" stroke-width="1.4"><path d="M1 3a7 7 0 0 1 10 0M3 5.5a4 4 0 0 1 6 0"/><circle cx="6" cy="8" r=".8" fill="#111"/></svg>
    <svg width="14" height="8" viewBox="0 0 14 8"><rect x=".5" y=".5" width="12" height="7" rx="1.5" fill="#111"/></svg>
  </div>
  <div class="small-dot" style="left:123px;top:42px"></div>
  <div class="small-name" style="left:0;top:70px">KovaPay</div>
  <div class="menu" style="left:9px;top:71px"></div>
  <div class="chat" style="left:229px;top:69px"></div>
  <svg style="left:253px;top:70px" width="11" height="13" viewBox="0 0 11 13" fill="none" stroke="#111" stroke-width="1.2"><circle cx="5.5" cy="4" r="3"/><path d="M1 12.5c0-3 2-4.5 4.5-4.5S10 9.5 10 12.5z"/></svg>

  <div class="stat" style="left:5px;top:106px;width:80px;height:33px"><div class="ico"></div><div class="lbl">Disbursed</div><div class="val">$30,000</div></div>
  <div class="stat" style="left:91px;top:106px;width:81px;height:33px"><div class="ico"></div><div class="lbl">Collected</div><div class="val">$50,000</div></div>
  <div class="stat" style="left:178px;top:106px;width:97px;height:33px"><div class="ico"></div><div class="lbl">Active Clients</div><div class="val">$60,000</div></div>
  <div class="stat" style="left:85px;top:147px;width:97px;height:33px"><div class="ico"></div><div class="lbl">New Clients</div><div class="val">$60,000</div></div>

  <div class="heading" style="left:7px;top:184px">Filters</div>
  <div class="chip" style="left:6px;top:210px;width:82px">Loan Officer</div>
  <div class="chip" style="left:95px;top:210px;width:61px">Branch</div>
  <div class="chip" style="left:161px;top:210px;width:48px">Fund</div>
  <div class="chip" style="left:215px;top:210px;width:56px">Product</div>

  <div class="row-ico" style="left:18px;top:249px"></div>
  <div class="row-lbl" style="left:51px;top:243px">Near Due</div>
  <div class="row-val" style="left:144px;top:243px">25,00,000</div>
  <div class="bar" style="top:264px"><div class="fill" style="width:57%"></div><div class="knob" style="left:57%"></div></div>

  <div class="row-ico" style="left:18px;top:288px"></div>
  <div class="row-lbl" style="left:51px;top:282px">Due</div>
  <div class="row-val" style="left:144px;top:282px">30,00,000</div>
  <div class="bar" style="top:303px"><div class="fill" style="width:73%"></div><div class="knob" style="left:73%"></div></div>

  <div class="row-ico" style="left:18px;top:331px"></div>
  <div class="row-lbl" style="left:51px;top:325px">Overdue</div>
  <div class="row-val" style="left:144px;top:325px">20,00,000</div>
  <div class="bar" style="top:346px"><div class="fill" style="width:49%"></div><div class="knob" style="left:49%"></div></div>

  <div class="row-ico" style="left:18px;top:375px"></div>
  <div class="row-lbl" style="left:51px;top:369px">Pending Disbursement</div>
  <div class="row-val" style="left:144px;top:369px">28,00,000</div>
  <div class="bar" style="top:390px"><div class="fill" style="width:68%"></div><div class="knob" style="left:68%"></div></div>

  <div class="row-ico" style="left:18px;top:417px"></div>
  <div class="row-lbl" style="left:51px;top:411px">Active Loans</div>
  <div class="row-val" style="left:144px;top:411px">22,00,000</div>
  <div class="bar" style="top:432px"><div class="fill" style="width:49%"></div><div class="knob" style="left:49%"></div></div>

  <div class="axis" style="left:22px;top:452px">$ 5.000</div>
  <div class="axis" style="left:22px;top:470px">$ 4.000</div>
  <div class="axis" style="left:22px;top:489px">$ 3.000</div>
  <div class="axis" style="left:22px;top:507px">$ 2.000</div>
  <div class="axis" style="left:22px;top:525px">$ 1.000</div>
  <div class="axis" style="left:22px;top:543px">0</div>
  <svg style="left:58px;top:457px" width="186" height="91" viewBox="0 0 240 120" preserveAspectRatio="none">
    <path d="M0 20C20 10 40 15 55 45C65 58 80 42 100 45C115 48 120 25 140 20C160 16 170 38 190 25C210 12 225 2 240 4L240 120L0 120Z" fill="var(--area-light)"/>
    <path d="M0 80C20 60 30 115 60 110C80 105 90 60 110 80C130 100 150 92 165 80C180 68 190 112 205 95C215 65 230 70 240 75L240 120L0 120Z" fill="var(--area-dark)"/>
    <path d="M0 20C20 10 40 15 55 45C65 58 80 42 100 45C115 48 120 25 140 20C160 16 170 38 190 25C210 12 225 2 240 4" fill="none" stroke="var(--blue)" stroke-width="2"/>
  </svg>
  <div class="tick" style="left:74px;top:559px">2022</div>
  <div class="tick" style="left:149px;top:559px">2023</div>
  <div class="tick" style="left:220px;top:559px">2024</div>

  <nav class="nav" style="left:15px;top:566px;width:255px">
    <div class="on" style="left:22px"></div>
    <svg class="it" style="left:22px;top:8px" viewBox="0 0 24 24" fill="none" stroke="#fff" stroke-width="1.6"><path d="M5 11l7-6 7 6v8H5z"/><path d="M10 19v-5h4v5"/></svg>
    <svg class="it" style="left:76px" viewBox="0 0 24 24" fill="none" stroke="#333" stroke-width="1.3"><path d="M9 5h6l-2 4h-2z"/><circle cx="12" cy="15" r="5.5"/><path d="M2 21h9"/></svg>
    <svg class="it" style="left:131px" viewBox="0 0 24 24" fill="none" stroke="#333" stroke-width="1.3"><rect x="5" y="4" width="14" height="17" rx="1.5"/><path d="M9 9h6M9 13h6M9 17h4"/></svg>
    <svg class="it" style="left:185px" viewBox="0 0 24 24" fill="none" stroke="#333" stroke-width="1.3"><rect x="5" y="3" width="14" height="18" rx="1"/><path d="M8 8h8M8 12h3M13 12h3M8 16h8"/></svg>
    <svg class="it" style="left:233px" viewBox="0 0 24 24" fill="none" stroke="#333" stroke-width="1.3"><circle cx="12" cy="12" r="3"/><circle cx="12" cy="12" r="7" stroke-dasharray="3 2"/></svg>
  </nav>
</section>

<!-- Loan summary -->
<section class="screen screen-summary">
  <div class="time" style="left:9px;top:37px">11:56 pm</div>
  <div class="status" style="left:222px;top:37px">
    <svg width="12" height="9" viewBox="0 0 12 9"><rect x="0" y="6" width="2" height="3"/><rect x="3" y="4" width="2" height="5"/><rect x="6" y="2" width="2" height="7"/><rect x="9" y="0" width="2" height="9"/></svg>
    <svg width="12" height="9" viewBox="0 0 12 9" fill="none" stroke="#111" stroke-width="1.4"><path d="M1 3a7 7 0 0 1 10 0M3 5.5a4 4 0 0 1 6 0"/><circle cx="6" cy="8" r=".8" fill="#111"/></svg>
    <svg width="14" height="8" viewBox="0 0 14 8"><rect x=".5" y=".5" width="12" height="7" rx="1.5" fill="#111"/></svg>
  </div>
  <div class="search">Search
    <svg style="left:214px;top:5px" width="10" height="10" viewBox="0 0 10 10" fill="none" stroke="#444" stroke-width="1.4"><circle cx="4" cy="4" r="3"/><path d="M6.5 6.5L9.5 9.5"/></svg>
  </div>
  <h1 class="title" style="left:0;top:92px">Loan Summary</h1>
  <div class="table">
    <div class="tr" style="top:0"><div class="row-ico"></div><div class="k">Loan reference number</div><div class="v">25450890</div></div>
    <div class="tr" style="top:43.2px"><div class="row-ico"></div><div class="k">Loan status</div><div class="v">Active</div></div>
    <div class="tr" style="top:86.4px"><div class="row-ico"></div><div class="k">Date disbursed</div><div class="v">03 07 2024</div></div>
    <div class="tr" style="top:129.6px"><div class="row-ico"></div><div class="k">Date approved</div><div class="v">07 07 2024</div></div>
    <div class="tr" style="top:172.8px"><div class="row-ico"></div><div class="k">Last repayment date</div><div class="v">10 07 2024</div></div>
    <div class="tr" style="top:216px"><div class="row-ico"></div><div class="k">Next repayment date</div><div class="v">12 07 2024</div></div>
    <div class="tr" style="top:259.2px"><div class="row-ico"></div><div class="k">Amount disbursed</div><div class="v">30,000</div></div>
    <div class="tr" style="top:302.4px"><div class="row-ico"></div><div class="k">Amount outstanding</div><div class="v">30,000</div></div>
    <div class="tr" style="top:345.6px;border-bottom:none"><div class="row-ico"></div><div class="k">Overdue days</div><div class="v">30</div></div>
  </div>
  <div class="next">NEXT</div>

  <nav class="nav" style="left:18px;top:571px;width:259px">
    <svg class="it" style="left:23px" viewBox="0 0 24 24" fill="none" stroke="#333" stroke-width="1.4"><path d="M5 11l7-6 7 6v8H5z"/><path d="M10 19v-5h4v5"/></svg>
    <svg class="it" style="left:77px" viewBox="0 0 24 24" fill="none" stroke="#333" stroke-width="1.3"><path d="M9 5h6l-2 4h-2z"/><circle cx="12" cy="15" r="5.5"/><path d="M2 21h9"/></svg>
    <div class="on" style="left:131px"></div>
    <svg class="it" style="left:131px" viewBox="0 0 24 24" fill="none" stroke="#fff" stroke-width="1.3"><rect x="5" y="4" width="14" height="17" rx="1.5"/><path d="M9 9h6M9 13h6M9 17h4"/></svg>
    <svg class="it" style="left:186px" viewBox="0 0 24 24" fill="none" stroke="#333" stroke-width="1.3"><rect x="5" y="3" width="14" height="18" rx="1"/><path d="M8 8h8M8 12h3M13 12h3M8 16h8"/></svg>
    <svg class="it" style="left:235px" viewBox="0 0 24 24" fill="none" stroke="#333" stroke-width="1.3"><circle cx="12" cy="12" r="3"/><circle cx="12" cy="12" r="7" stroke-dasharray="3 2"/></svg>
  </nav>
</section>

<!-- Total loan -->
<section class="screen screen-total">
  <div class="time" style="left:12px;top:26px">11:56 pm</div>
  <div class="status" style="left:214px;top:26px">
    <svg width="12" height="9" viewBox="0 0 12 9"><rect x="0" y="6" width="2" height="3"/><rect x="3" y="4" width="2" height="5"/><rect x="6" y="2" width="2" height="7"/><rect x="9" y="0" width="2" height="9"/></svg>
    <svg width="12" height="9" viewBox="0 0 12 9" fill="none" stroke="#111" stroke-width="1.4"><path d="M1 3a7 7 0 0 1 10 0M3 5.5a4 4 0 0 1 6 0"/><circle cx="6" cy="8" r=".8" fill="#111"/></svg>
    <svg width="14" height="8" viewBox="0 0 14 8"><rect x=".5" y=".5" width="12" height="7" rx="1.5" fill="#111"/></svg>
  </div>
  <div class="menu" style="left:13px;top:58px"></div>
  <h1 class="big" style="left:0;top:52px;font-size:19px;width:264px">Total Loan</h1>
  <div class="big" style="left:0;top:82px;font-size:14px;font-weight:700">$35,00,000</div>
  <div class="chat" style="left:216px;top:55px"></div>
  <svg style="left:250px;top:56px" width="11" height="13" viewBox="0 0 11 13" fill="none" stroke="#111" stroke-width="1.2"><circle cx="5.5" cy="4" r="3"/><path d="M1 12.5c0-3 2-4.5 4.5-4.5S10 9.5 10 12.5z"/></svg>

  <div class="heading" style="left:13px;top:133px">Filters</div>
  <div class="chip" style="left:12px;top:159px;width:79px">Loan Officer</div>
  <div class="chip" style="left:97px;top:159px;width:60px">Branch</div>
  <div class="chip" style="left:161px;top:159px;width:46px">Fund</div>
  <div class="chip" style="left:213px;top:159px;width:53px">Product</div>

  <div class="toggle"><div class="p">Profit</div><div class="l">Loss</div></div>
  <div class="pill" style="left:41px;width:42px">Day</div>
  <div class="pill" style="left:92px;width:46px">Week</div>
  <div class="pill sel" style="left:146px;width:48px">Month</div>
  <div class="pill" style="left:204px;width:41px">Year</div>

  <div class="tip"><div class="a">Interest</div><div class="b">$3,50,000</div></div>

  <div class="axis" style="left:28px;top:302px">$ 5.000</div>
  <div class="axis" style="left:28px;top:320px">$ 4.000</div>
  <div class="axis" style="left:28px;top:339px">$ 3.000</div>
  <div class="axis" style="left:28px;top:358px">$ 2.000</div>
  <div class="axis" style="left:28px;top:377px">$ 1.000</div>
  <div class="axis" style="left:28px;top:395px">0</div>
  <svg style="left:62px;top:309px" width="186" height="92" viewBox="0 0 240 120" preserveAspectRatio="none">
    <path d="M60 0V120M120 0V120M180 0V120" stroke="#e8eaed" stroke-width="1"/>
    <path d="M0 22C20 12 40 15 55 45C65 60 80 42 100 45C115 48 120 25 140 22C160 18 170 38 190 28C210 18 225 8 240 10L240 120L0 120Z" fill="var(--area-light)"/>
    <path d="M0 80C20 60 30 115 60 110C80 105 90 60 110 80C130 100 150 92 165 80C180 68 190 112 205 95C215 65 230 70 240 75L240 120L0 120Z" fill="var(--area-dark)"/>
    <path d="M0 22C20 12 40 15 55 45C65 60 80 42 100 45C115 48 120 25 140 22C160 18 170 38 190 28C210 18 225 8 240 10" fill="none" stroke="var(--blue)" stroke-width="2"/>
  </svg>
  <div style="left:169px;top:306px;width:16px;height:16px;border-radius:50%;background:#5fd49a"></div>
  <div class="tick" style="left:58px;top:408px">Week 01</div>
  <div class="tick" style="left:106px;top:408px">Week 02</div>
  <div class="tick" style="left:156px;top:408px">Week 03</div>
  <div class="tick" style="left:217px;top:408px">Week 04</div>

  <div class="stat" style="left:15px;top:428px;width:87px;height:36px"><div class="ico" style="top:9px"></div><div class="lbl" style="top:7px">Revenue</div><div class="val" style="top:19px">$30,000</div></div>
  <div class="stat" style="left:108px;top:428px;width:87px;height:36px"><div class="ico" style="top:9px"></div><div class="lbl" style="top:7px">Expenses</div><div class="val" style="top:19px">$50,000</div></div>
  <div class="stat" style="left:17px;top:473px;width:87px;height:36px"><div class="ico" style="top:9px"></div><div class="lbl" style="top:7px">Tax</div><div class="val" style="top:19px">$60,000</div></div>
  <div class="stat" style="left:112px;top:473px;width:91px;height:36px"><div class="ico" style="top:9px"></div><div class="lbl" style="top:7px">Salaries</div><div class="val" style="top:19px">$60,000</div></div>

  <nav class="nav" style="left:19px;top:535px;width:248px">
    <svg class="it" style="left:22px" viewBox="0 0 24 24" fill="none" stroke="#333" stroke-width="1.4"><path d="M5 11l7-6 7 6v8H5z"/><path d="M10 19v-5h4v5"/></svg>
    <svg class="it" style="left:74px" viewBox="0 0 24 24" fill="none" stroke="#333" stroke-width="1.3"><path d="M9 5h6l-2 4h-2z"/><circle cx="12" cy="15" r="5.5"/><path d="M2 21h9"/></svg>
    <svg class="it" style="left:125px" viewBox="0 0 24 24" fill="none" stroke="#333" stroke-width="1.3"><rect x="5" y="4" width="14" height="17" rx="1.5"/><path d="M9 9h6M9 13h6M9 17h4"/></svg>
    <div class="on" style="left:178px"></div>
    <svg class="it" style="left:178px" viewBox="0 0 24 24" fill="none" stroke="#fff" stroke-width="1.3"><rect x="5" y="3" width="14" height="18" rx="1"/><path d="M8 8h8M8 12h3M13 12h3M8 16h8"/></svg>
    <svg class="it" style="left:225px" viewBox="0 0 24 24" fill="none" stroke="#333" stroke-width="1.3"><circle cx="12" cy="12" r="3"/><circle cx="12" cy="12" r="7" stroke-dasharray="3 2"/></svg>
  </nav>
</section>

</body>
</html>
```